New Flyer Design Project

Update of our festival form for 2020. We want a form that is as clean looking as possible with as much information on the form as possible. We would like the form to be fillable and have a running total at the bottom. I must be able to update information on the forms. We want to include a statement.
COVID-19, We are following the Office for Public Wellness and Readiness, and state and local guidelines to stay safe from COVID-19. While attending this meeting, please follow all posted instructions. If you are sick, please stay home. Cover your cough and sneezes. Feel free to wear a mask. Let's help each other stay safe and healthy. By attending, you voluntarily assume all risk related to exposure.

Our partners compete to raise the most funds for our organization. If it's possible to put a breakout in the form of who the vendor is sponsoring, that would be great. For example: some vendors sponsor one or two companies, some sponsor 4 and a few sponsors all 8. Another item we need to highlight, most people sign up for the event to sponsor and not attend. Make it as obvious as possible if you're not attending . We need the names of the people attending only.

Dates to be changed:
1. Change event to 22nd Annual DWT festival (both pages)
2. Change event date to October 3rd 2020 (both pages are locations)
3. Change hotel reservations due by: September 1st (both pages )
4. Bluegrass tours change date to Oct 3rd
5. Golf change date to Oct 3rd and add Saturday, Oct
6. Change registration deadline to October 1, 2020

```html
<!DOCTYPE html>
<html lang="en">
<head>
<meta charset="utf-8">
<title>22nd Annual DWT Festival – Registration Form</title>
<link href="https://fonts.googleapis.com/css2?family=Roboto:wght@400;500;700&family=Roboto+Condensed:ital,wght@0,400;0,700;1,700&display=swap" rel="stylesheet">
<style>
:root{
  --red:#a50b0b;
  --bright-red:#d40f0f;
  --ink:#1d1d1d;
  --rule:#2a2a2a;
  --stripe:#e4e4e4;
  --panel:#ebebeb;
  --backdrop:#e2e2e2;
}
*{box-sizing:border-box;margin:0;padding:0}
html,body{width:1200px;height:1200px;overflow:hidden;background:var(--backdrop)}
body{font-family:"Roboto Condensed",sans-serif;color:var(--ink)}
.sheet{position:absolute;left:210px;top:21px;width:1220px;height:1810px;background:#fff;transform:scale(.64);transform-origin:0 0;box-shadow:0 6px 18px rgba(0,0,0,.18)}
.brand{position:absolute;left:70px;top:150px;display:flex;align-items:center;gap:12px;font-size:36px;font-weight:700;color:var(--ink);white-space:nowrap}
.brand-dot{width:24px;height:24px;border-radius:50%;background:var(--ink)}
.title{position:absolute;left:388px;top:62px;width:758px;font-family:"Roboto Condensed",sans-serif;font-weight:700;font-size:76px;color:var(--red);line-height:1;white-space:nowrap;padding-bottom:2px;border-bottom:3px solid var(--red)}
.date{position:absolute;left:388px;top:148px;font-family:"Roboto",sans-serif;font-weight:500;font-size:44px;white-space:nowrap}
.venue{position:absolute;left:392px;top:206px;font-family:"Roboto",sans-serif;font-size:32px;color:var(--bright-red);white-space:nowrap}
.banner{position:absolute;left:55px;top:269px;width:1110px;height:42px;border-radius:21px;background:var(--red);color:#fff;text-align:center;font-family:"Roboto",sans-serif;font-weight:500;font-size:31px;line-height:42px}
.box{position:absolute;border:1.5px solid var(--rule);background:#fff}
.box-head{background:var(--red);color:#fff;font-weight:700;font-size:24px;height:31px;line-height:31px;padding:0 10px;white-space:nowrap}
.box-head small{font-weight:400;font-size:17px}
.row{display:flex;align-items:flex-end;gap:8px;font-size:22px;line-height:1.2;white-space:nowrap}
.line{flex:1;border-bottom:1.5px solid var(--rule);margin-bottom:6px}
.bold{font-weight:700}
.red{color:var(--red)}
.check{display:inline-block;width:12px;height:12px;border:1.5px solid var(--rule);margin:0 10px 6px 0;flex:none}

.contact{left:60px;top:330px;width:541px;height:134px;padding:22px 10px 0}
.contact .row{margin-bottom:11px}

.guests{left:60px;top:477px;width:541px;height:236px}
.guests .box-head{height:56px;display:flex;align-items:center;gap:8px}
.guests .box-head .note{font-weight:400;font-size:13.5px;line-height:1.15;border-left:1.5px solid #fff;padding-left:8px}
.guest-list{position:absolute;left:12px;top:100px;width:296px}
.guest-list .row{margin-bottom:7px;font-size:21px}
.credit{position:absolute;left:328px;top:68px;width:202px;height:156px;background:var(--panel);border-radius:12px;padding:8px 10px 0;text-align:center}
.credit p{font-size:13.5px;color:var(--bright-red);line-height:1.25;margin-bottom:4px}
.credit .line{height:26px;margin:0}

.banquet{left:60px;top:732px;width:541px;height:221px}
.banquet .inner{padding:10px 10px 0}
.banquet .row{margin-bottom:9px}
.sub-head{font-weight:700;font-size:24px;color:var(--red);margin:2px 0 6px}
.indent{padding-left:18px}

.tours{left:60px;top:973px;width:541px;height:201px}
.tours .inner{padding:7px 11px 0}
.tours p{font-size:21px;line-height:1.35;margin-bottom:10px;white-space:nowrap}
.tours .row{margin-bottom:12px}

.deadline{position:absolute;left:60px;top:1196px;width:541px;height:328px;background:var(--panel);text-align:center;padding-top:14px;font-size:19.5px;line-height:1.3}
.deadline h3{font-size:25px;color:var(--red);font-weight:700;margin-bottom:4px}
.deadline .gap{margin-top:10px}
.deadline hr{width:378px;margin:14px auto 14px;border:0;border-top:1.5px solid var(--rule)}

.questions{position:absolute;left:0;top:1548px;width:601px;height:138px;background:var(--red);border-radius:0 30px 30px 0;color:#fff;text-align:center;font-weight:700;padding-top:12px}
.questions h2{font-style:italic;font-size:38px;line-height:1.1}
.questions p{font-size:24px;line-height:1.35}

.sponsors{left:623px;top:330px;width:533px;height:226px}
.sponsor-row{display:flex;align-items:center;height:36.5px;padding:0 20px 0 14px;font-size:22px}
.sponsor-row .check{margin-bottom:0}
.sponsor-row.shaded{background:var(--stripe)}
.sponsor-row .price{margin-left:auto}

.golf{left:623px;top:577px;width:533px;height:328px}
.golf .box-head{font-size:23px}
.golf .inner{padding:8px 18px 0 11px}
.golf .row{margin-bottom:16px}
.golf .pair{display:flex;gap:12px;margin-bottom:10px}
.golf .pair .row{flex:1;margin:0}

.spa{left:623px;top:922px;width:533px;height:377px}
.spa .intro{background:var(--stripe);font-size:18.5px;line-height:1.2;padding:10px 11px}
.spa .inner{padding:10px 18px 0 11px}
.spa .row{margin-bottom:14px}
.spa .pref{font-size:19px;margin-bottom:12px}
.spa .massage{font-size:21px;color:var(--bright-red);padding-left:46px;display:flex;align-items:center;margin-bottom:14px;white-space:nowrap}
.spa .massage .check{margin-bottom:0}

.card{left:623px;top:1326px;width:533px;height:198px;padding:20px 18px 0 11px}
.card .row{margin-bottom:19px}

.total{left:623px;top:1548px;width:533px;height:138px;padding:20px 22px 0}
.total .row{font-size:25px;font-weight:700;color:var(--red);margin-bottom:18px}
.total .line{border-color:var(--red)}
.total p{text-align:center;font-size:18.5px;line-height:1.3}

.health{position:absolute;left:60px;top:1704px;width:1096px;height:88px;border:1.5px solid var(--rule);padding:8px 12px;font-size:17px;line-height:1.3}
.health b{color:var(--red)}
</style>
</head>
<body>
<main class="sheet">
  <div class="brand"><span class="brand-dot"></span>Dale Wing Trust</div>
  <h1 class="title">22nd Annual DWT Festival</h1>
  <div class="date">Saturday, October 3, 2020</div>
  <div class="venue">Harbor Gate Inn, Lexington</div>
  <div class="banner">REGISTRATION FORM</div>

  <section class="box contact">
    <div class="row">Company/Contact<span class="line"></span></div>
    <div class="row">Email <span class="line"></span></div>
    <div class="row">Best Phone<span class="line"></span></div>
  </section>

  <section class="box guests">
    <div class="box-head">Guest Names <span class="note">As they should appear on name badges. Fill out only for<br>those planning to attend.</span></div>
    <div class="guest-list">
      <div class="row">1.<span class="line"></span></div>
      <div class="row">2.<span class="line"></span></div>
      <div class="row">3.<span class="line"></span></div>
      <div class="row">4.<span class="line"></span></div>
    </div>
    <div class="credit">
      <p>If not attending, who get credit<br>for your sponsorship dollars.</p>
      <div class="line"></div><div class="line"></div><div class="line"></div><div class="line"></div>
    </div>
  </section>

  <section class="box banquet">
    <div class="box-head">Awards Banquet and Monte Carlo Night</div>
    <div class="inner">
      <div class="row"># of Tickets <span class="line"></span> x $150 <span class="line"></span></div>
      <div class="sub-head">Static Trade Show Booth Requests</div>
      <div class="row indent">Trade Show Booth (8ft Table)<span class="line"></span>$100</div>
      <div class="row indent">Additional Table<span class="line"></span> $50</div>
      <div class="row"><span class="bold">Total</span><span class="line" style="flex:3"></span>$ <span class="line"></span></div>
    </div>
  </section>

  <section class="box tours">
    <div class="box-head">Blue Grass Tours</div>
    <div class="inner">
      <p>Horse Farm, Hooch and History Tour. <b>Saturday, Oct 3.</b><br>Bus leaves at <b>9.30AM,</b> returns <b>2.15PM. Limited Seats Available</b></p>
      <div class="row"># of Reservations<span class="line"></span> x $150 <span class="line"></span></div>
      <div class="row"><span class="bold">Total Tour</span><span class="line"></span><b>$</b> <span class="line"></span></div>
    </div>
  </section>

  <section class="deadline">
    <h3>DEADLINE FOR REGISTRATION: OCTOBER 1, 2020</h3>
    <p>Make checks payable to the Dale Wing Trust or pay<br>via credit card using this form.</p>
    <p class="gap">Mail payment and this registration form to<br><b>1180 College Station, Murray, KY 42071</b></p>
    <hr>
    <h3>RESERVE YOUR HOTEL ROOM EARLY !</h3>
    <p><b>Call Harbor Gate</b><br>at <b>(859) 555-0188 by September 1st</b><br>to make your room reservations. Mention the Dale Wing<br>Trust or DWT for your room block</p>
  </section>

  <section class="questions">
    <h2>QUESTIONS ?</h2>
    <p>Contact Jordan Pell at 270.555.0142<br>jpell@dwtfest.org</p>
  </section>

  <section class="box sponsors">
    <div class="box-head">Sponsorships</div>
    <div>
      <div class="sponsor-row"><span class="check"></span>Diamond Sponsor<span class="price">$5,000</span></div>
      <div class="sponsor-row shaded"><span class="check"></span>Golden Egg Sponsor<span class="price">$3,000</span></div>
      <div class="sponsor-row"><span class="check"></span>Silver Chicken Sponsor<span class="price">$2,000</span></div>
      <div class="sponsor-row shaded"><span class="check"></span>Bronze Turkey Sponsor<span class="price">$1,000</span></div>
      <div class="sponsor-row"><span class="check"></span>Friend of DWT<span class="price">$500</span></div>
    </div>
  </section>

  <section class="box golf">
    <div class="box-head">Best Ball Golf Scramble <small>(Saturday, Oct 3 · Limit 120, Lunch incl.)</small></div>
    <div class="inner">
      <div class="row"># of Players <span class="line" style="flex:2.2"></span> x $100 <span class="line"></span></div>
      <div class="row"># of Team Players <span class="line" style="flex:1.7"></span> x $125 <span class="line"></span></div>
      <div class="row"><span class="check" style="margin-right:6px"></span>Team of 4 Players<span class="line" style="flex:1.5"></span> $500 <span class="line"></span></div>
      <div class="pair"><div class="row">1.<span class="line"></span></div><div class="row">2.<span class="line"></span></div></div>
      <div class="pair"><div class="row">3.<span class="line"></span></div><div class="row">4.<span class="line"></span></div></div>
      <div class="row"><span class="bold">Golf Total</span><span class="line"></span>$<span class="line" style="flex:1.55"></span></div>
      <div class="row"><span class="bold">Average Score</span><span class="line"></span></div>
    </div>
  </section>

  <section class="box spa">
    <div class="box-head">Spa Day</div>
    <div class="intro">Limited appointments available from 8am to 4pm. Slots will be filled on a first come first served basis. We will contact you before the event to confirm your appointment</div>
    <div class="inner">
      <div class="row">Name(s) <span class="line"></span></div>
      <div class="row"><span class="bold red" style="font-size:24px">Day Phone</span> <span class="line"></span></div>
      <div class="row"># of Reservations<span class="line"></span> x $150 <span class="line" style="flex:.7"></span></div>
      <div class="pref">Circle Time Preference:</div>
      <div class="massage"><span class="check"></span>Massage : Early AM, late AM, early PM or late PM</div>
      <div class="row"><span class="bold">Spa Day Total</span><span class="line"></span><b>$</b> <span class="line"></span></div>
    </div>
  </section>

  <section class="box card">
    <div class="row">Credit Card# <span class="line"></span></div>
    <div class="row">Name on Card <span class="line"></span></div>
    <div class="row">Exp. Date <span class="line"></span> CVC <span class="line"></span></div>
    <div class="row">Billing Zip Code<span class="line"></span></div>
  </section>

  <section class="box total">
    <div class="row">Total Payment to DWT$<span class="line"></span></div>
    <p>Sponsorship, Banquet and Entertainment Tickets, Trade Show<br>Golf Scramble, Farm and Distillery Tour &amp; Spa Day</p>
  </section>

  <section class="health">
    <b>COVID-19</b> We are following the Office for Public Wellness and Readiness, and state and local guidelines to stay safe from COVID-19. While attending this meeting, please follow all posted instructions. If you are sick, please stay home. Cover your cough and sneezes. Feel free to wear a mask. Let's help each other stay safe and healthy. By attending, you voluntarily assume all risk related to exposure.
  </section>
</main>
</body>
</html>
```